Maple Meadow Nectar and Combs produces and sells local raw honey.

The logo is in the files. Use the one with the brown letters. We are looking to have a web page that tells our customers about our products and where they can be purchased. We may take orders and sell from this web page in the future. We would like to have a way for customers to ask questions or provide feedback. I've provided pictures but it will be up to the designer's discretion to use whatever pictures are relevant to the design.

Target Market(s)

Customers in the greater Seattle area.

Coding

Coded - Design and coding required

Number of Pages Required

3 page

Font styles to use
Sans Serif

Colors

Designer to choose colors to be used in the design.

Requirements
Must have
• A message that we produce and sell only pure raw local honey. Raw honey means it has never been flavored, heated, pasteurized, filtered or has additives of any kind. The web page should also let people know where they can find our honey for purchase.

```html
<!DOCTYPE html>
<html lang="en">
<head>
<meta charset="utf-8">
<title>Maple Meadow Nectar – Pure Raw Local Honey</title>
<link href="https://fonts.googleapis.com/css2?family=Raleway:wght@300;400;500;600;700&family=Open+Sans:wght@400;600&display=swap" rel="stylesheet">
<style>
:root{
  --gold:#f2d400;
  --gold-deep:#e0c200;
  --ink:#222222;
  --muted:#555555;
  --cream:#fdf8e4;
  --footer:#232323;
  --white:#ffffff;
}
*{margin:0;padding:0;box-sizing:border-box}
html,body{width:1200px;height:2830px;overflow:hidden;background:var(--white)}
body{position:relative;font-family:'Raleway',sans-serif;color:var(--ink)}
.abs{position:absolute}
.body-copy{font-family:'Open Sans',sans-serif;font-size:11.5px;line-height:20px;color:var(--muted)}

/* header */
.site-header{left:0;top:0;width:1200px;height:128px;background:var(--white)}
.brand{left:160px;top:44px;display:flex;align-items:center;gap:10px;font-size:19px;font-weight:600;color:#5a3b1a}
.brand-mark{width:26px;height:26px;border-radius:50%;background:var(--gold)}
.search{left:755px;top:22px;width:283px;height:40px;background:#eeeeee;display:flex;align-items:center;padding:0 14px;font-size:11px;color:#777;justify-content:space-between}
.main-nav{left:410px;top:84px;width:630px;display:flex;justify-content:space-between;font-size:13.5px;font-weight:600}
.main-nav .active{color:var(--gold)}

/* hero */
.hero{left:0;top:128px;width:1200px;height:474px;background:linear-gradient(180deg,#6b6a55 0%,#8c7f64 45%,#7a6a52 100%)}
.hero h1{left:0;top:150px;width:1200px;text-align:center;color:var(--white);font-size:44px;font-weight:600;line-height:46px}
.btn{background:var(--gold);color:var(--white);font-size:12px;font-weight:700;border-radius:20px;text-align:center}
.hero .btn{left:535px;top:266px;width:130px;height:36px;line-height:36px}
.dots{left:560px;top:420px;display:flex;gap:5px}
.dots span{width:18px;height:18px;border-radius:50%;background:var(--white)}
.dots span.on{background:var(--gold)}

/* about */
.about{left:0;top:602px;width:1200px;height:368px;background:linear-gradient(180deg,#ffffff 0%,#ffffff 65%,#f2f0ea 100%)}
.about h2{left:550px;top:80px;font-size:36px;font-weight:400}
.about .lead{left:550px;top:140px;width:490px;font-family:'Open Sans',sans-serif;font-size:11.5px;font-weight:600}
.about .body-copy{left:550px;top:166px;width:490px}

/* purchase */
.purchase{left:0;top:970px;width:670px;height:376px;background:var(--gold)}
.purchase h2{left:160px;top:70px;font-size:36px;font-weight:300;line-height:44px;color:var(--white)}
.purchase .body-copy{left:160px;top:166px;width:500px;color:var(--white)}
.purchase-photo{left:670px;top:970px;width:530px;height:376px;background:linear-gradient(180deg,#4a8fd6 0%,#9cc4e8 28%,#3f5a3a 45%,#b06fa8 62%,#3d6a2e 100%)}

/* varieties */
.varieties-title{left:0;top:1378px;width:1200px;text-align:center;font-size:36px;font-weight:400}
.variety{top:1456px;width:202px;text-align:center}
.variety .thumb{width:202px;height:216px;border:1px solid var(--gold)}
.variety h3{margin-top:16px;font-size:17px;font-weight:700}
.variety p{margin-top:6px;font-size:13.5px}
.arrow{top:1546px}

/* swarm */
.swarm{left:0;top:1787px;width:1200px;height:359px;background:radial-gradient(ellipse at center,#7a5a2a 0%,#5a4020 60%,#3a2a15 100%)}
.swarm h2{left:0;top:112px;width:1200px;text-align:center;color:var(--white);font-size:30px;font-weight:700;line-height:40px}
.swarm .contact{left:0;top:205px;width:1200px;text-align:center;color:var(--gold);font-size:32px;font-weight:700}

/* calendar */
.calendar{left:0;top:2146px;width:1200px;height:409px;background:var(--cream)}
.calendar h2{left:0;top:34px;width:1200px;text-align:center;font-size:36px;font-weight:400}
.season{top:108px;height:238px}
.season .card{position:absolute;background:var(--white);padding:28px 24px}
.season h3{font-size:17px;font-weight:500;margin-bottom:18px}
.winter{left:160px;width:278px;background:linear-gradient(135deg,#2f3a22,#4a3a22)}
.winter .card{left:18px;top:21px;width:240px;height:194px}
.summer{left:478px;width:560px;background:var(--gold)}
.summer .card{left:12px;top:21px;width:528px;height:196px}
.season .body-copy{font-size:11px;line-height:23px}

/* footer */
.site-footer{left:0;top:2555px;width:1200px;height:275px;background:var(--footer);color:#cfcfcf}
.fcol{top:48px;font-family:'Open Sans',sans-serif;font-size:11px;line-height:19px}
.fcol h4{font-family:'Raleway',sans-serif;font-size:13.5px;font-weight:600;color:var(--white);margin-bottom:14px}
.fcol .gap{margin-top:14px}
.fcol .hl{color:var(--gold)}
.newsletter{left:745px;top:84px;width:293px;height:36px;display:flex}
.newsletter span{flex:1;background:var(--white);font-size:10px;color:#777;padding:0 10px;line-height:36px;font-style:italic}
.newsletter b{width:74px;background:var(--gold);color:var(--ink);font-size:11px;text-align:center;line-height:36px}
.socials{left:745px;top:152px;display:flex;gap:8px}
.legal{left:745px;top:212px;font-family:'Open Sans',sans-serif;font-size:10.5px;line-height:22px;color:var(--white)}
</style>
</head>
<body>

<header class="abs site-header">
  <div class="abs brand"><span class="brand-mark"></span>Maple Meadow Nectar</div>
  <div class="abs search"><span>Enter keyword</span>
    <svg width="12" height="12" viewBox="0 0 12 12"><circle cx="5" cy="5" r="3.8" fill="none" stroke="#222" stroke-width="1.6"/><line x1="8" y1="8" x2="11" y2="11" stroke="#222" stroke-width="1.8"/></svg>
  </div>
  <nav class="abs main-nav"><span class="active">Home</span><span>Farmers</span><span>Information</span><span>Products</span><span>Honey</span><span>About Us</span><span>Contact</span></nav>
</header>

<section class="abs hero" role="img" aria-label="Beehive boxes strapped together on a dry hillside apiary">
  <h1 class="abs">We sell only pure<br>raw local honey</h1>
  <div class="abs btn">READ MORE</div>
  <div class="abs dots"><span></span><span class="on"></span><span class="on"></span><span></span></div>
</section>

<section class="abs about">
  <svg class="abs" style="left:150px;top:12px" width="260" height="340" viewBox="0 0 260 340" role="img" aria-label="Honeycomb-shaped photos of hive frames, a honey jar and bees on comb">
    <polygon points="160,6 218,38 218,104 160,136 102,104 102,38" fill="#6f6a5e" stroke="#f2d400" stroke-width="3"/>
    <polygon points="78,142 136,174 136,240 78,272 20,240 20,174" fill="#4a3a2a" stroke="#f2d400" stroke-width="3"/>
    <polygon points="198,142 256,174 256,240 198,272 140,240 140,174" fill="#9a6a2a" stroke="#f2d400" stroke-width="3"/>
  </svg>
  <h2 class="abs">About Our Products</h2>
  <p class="abs lead">Maple Meadow Nectar and Combs LLC is located at 14310 Cedar Ridge Rd. Woodinville, WA.</p>
  <p class="abs body-copy">We sell raw local honey and beeswax candles at our apiary/farm as well as honey at farmers markets and small stores that specialize in locally grown and produced products. Our usual honey varietals include: Big Leaf Maple, Pacific NW Fireweed, Blackberry Blossom, Japanese Knotweed, Blueberry Blossom, Raspberry Blossom and Woodinville Wildflower. We also sell a raw creamed honey as well as cut comb honey.</p>
</section>

<section class="abs purchase">
  <h2 class="abs">Where they can be<br>Purchased.</h2>
  <p class="abs body-copy">Sed ut perspiciatis unde omnis iste natus error sit voluptatem accusantium doloremque laudantium, totam rem aperiam, eaque ipsa quae ab illo inventore veritatis et quasi architecto beatae vitae dicta sunt explicabo. Nemo enim ipsam voluptatem quia voluptas sit aspernatur. Sed ut perspiciatis unde omnis iste natus error sit voluptatem accusantium doloremque laudantium, totam rem aperiam, eaque ipsa quae ab illo inventore veritatis et quasi architecto beatae vitae dicta sunt explicabo. Nemo enim ipsam voluptatem quia.</p>
</section>
<div class="abs purchase-photo" role="img" aria-label="Mountain meadow of pink fireweed under a blue sky"></div>

<h2 class="abs varieties-title">Honey Varieties</h2>
<svg class="abs arrow" style="left:118px" width="20" height="34" viewBox="0 0 20 34"><polyline points="16,2 4,17 16,32" fill="none" stroke="#999" stroke-width="2"/></svg>
<svg class="abs arrow" style="left:1070px" width="20" height="34" viewBox="0 0 20 34"><polyline points="4,2 16,17 4,32" fill="none" stroke="#999" stroke-width="2"/></svg>
<div class="abs variety" style="left:160px"><div class="thumb" role="img" aria-label="White blackberry blossoms" style="background:linear-gradient(135deg,#3d5a2a,#8aa070 50%,#2e4a20)"></div><h3>Blackberry</h3><p>Read More</p></div>
<div class="abs variety" style="left:386px"><div class="thumb" role="img" aria-label="Big leaf maple flower cluster" style="background:linear-gradient(135deg,#2a2a18,#8a8a30 50%,#3a3a20)"></div><h3>Big Leaf Maple</h3><p>Read More</p></div>
<div class="abs variety" style="left:610px"><div class="thumb" role="img" aria-label="Field of colourful wildflowers" style="background:linear-gradient(135deg,#c84a3a,#e0a030 35%,#7a3a8a 65%,#4a7a30)"></div><h3>Wildflower</h3><p>Read More</p></div>
<div class="abs variety" style="left:836px"><div class="thumb" role="img" aria-label="Pink fireweed stalks by the water" style="background:linear-gradient(135deg,#8ab8d8,#c060a0 55%,#5a7a40)"></div><h3>Fireweed</h3><p>Read More</p></div>

<section class="abs swarm" role="img" aria-label="Blurred close-up of bees on golden honeycomb">
  <h2 class="abs">We offer free honey bee swarm removal<br>service within 30 miles of Woodinville.</h2>
  <div class="abs contact">Glen Harvey 206 555-0184</div>
</section>

<section class="abs calendar">
  <h2 class="abs">Calendar of Farmers Markets:</h2>
  <div class="abs season winter" role="img" aria-label="Dark honeycomb photo frame">
    <div class="card"><h3>Winter:</h3><p class="body-copy">Sundays at Capital Hill<br>(Broadway) in Seattle 11-3.</p></div>
  </div>
  <div class="abs season summer">
    <div class="card"><h3>Summer:</h3><p class="body-copy">Markets will begin in May and run through September.<br>Wednesdays 3-7 Mukilteo Park near the boat ramp.<br>Saturdays 9-3 Woodinville at Alder Creek Park north of Fernbrook Nursery.<br>Sundays to be announced.</p></div>
  </div>
</section>

<footer class="abs site-footer">
  <div class="abs fcol" style="left:160px">
    <h4>Contact</h4>
    <p>Address<br>Maple Meadow Nectar<br>14310 Cedar Ridge Rd.<br>Woodinville</p>
    <p class="gap">Contact: Maple Meadow Nectar<br><span class="hl">+1 206 555 0139</span><br>info@maplemeadownectar.com</p>
  </div>
  <div class="abs fcol" style="left:363px">
    <h4>Stores</h4><p>Locate a Store<br>Store Events<br>Our Services</p>
    <h4 class="gap">Resources</h4><p>What's New<br>Gift Cards<br>Site Map</p>
  </div>
  <div class="abs fcol" style="left:543px">
    <h4>Our Company</h4><p>About Us<br>Environmental Commitment<br>Careers<br>Press<br>Legal Statement<br>Privacy Policy<br>Terms &amp; Conditions</p>
  </div>
  <div class="abs fcol" style="left:745px"><h4>Newsletter</h4></div>
  <div class="abs newsletter"><span>Email Address:</span><b>SIGN UP</b></div>
  <div class="abs socials">
    <svg width="36" height="38" viewBox="0 0 36 38"><polygon points="18,1 34,10 34,28 18,37 2,28 2,10" fill="#f2d400"/></svg>
    <svg width="36" height="38" viewBox="0 0 36 38"><polygon points="18,1 34,10 34,28 18,37 2,28 2,10" fill="#f2d400"/></svg>
    <svg width="36" height="38" viewBox="0 0 36 38"><polygon points="18,1 34,10 34,28 18,37 2,28 2,10" fill="#f2d400"/></svg>
    <svg width="36" height="38" viewBox="0 0 36 38"><polygon points="18,1 34,10 34,28 18,37 2,28 2,10" fill="#f2d400"/></svg>
  </div>
  <p class="abs legal">Privacy Policy &nbsp;|&nbsp; Terms of Use &nbsp;|&nbsp; Site Map &nbsp;|&nbsp; Live Chat<br>© 2018 Maple Meadow Nectar. All Rights Reserved</p>
</footer>

</body>
</html>
```